Tellwick Asset Management - Corporate Letter Head Project

Looking for a classy design based on our current logo. Please find current logo source file in files. With our color scheme.

Target Market(s)

We're an investment firm, the letterhead needs to look professional and attractive to clients.

Industry/Entity Type

Hedgefund

Colors
0054AA
0677BA
7BADD7
CADEEF
E8F1F8

Requirements
Must have
• Our logo, address, phone number, and email

```html
<!DOCTYPE html>
<html lang="en">
<head>
<meta charset="utf-8">
<title>Tellwick Asset Management – Letterhead</title>
<link rel="stylesheet" href="https://fonts.googleapis.com/css2?family=Lato:wght@400;700&family=Kaushan+Script&display=swap">
<style>
  :root {
    --backdrop: #e8e9eb;
    --paper: #ffffff;
    --navy: #1c2b4f;
    --ink: #2a2a2a;
    --muted: #4a4a4a;
    --rule-grey: #b9bbbf;
  }
  * { margin: 0; padding: 0; box-sizing: border-box; }
  html, body {
    width: 1200px; height: 874px; overflow: hidden;
    background: var(--backdrop);
  }
  .letterhead {
    position: absolute; left: 300px; top: 13px;
    width: 600px; height: 848px;
    background: var(--paper);
    box-shadow: 0 2px 10px rgba(0,0,0,0.08);
    font-family: "Lato", sans-serif;
    color: var(--ink);
    overflow: hidden;
  }
  .brand {
    position: absolute; left: 40px; top: 52px;
    display: flex; align-items: center; gap: 10px;
  }
  .brand-square { width: 22px; height: 22px; background: var(--navy); }
  .brand-name {
    font-size: 17px; font-weight: 700; color: var(--navy); letter-spacing: 0.5px;
  }
  .contact {
    position: absolute; left: 400px; top: 40px;
    padding-left: 12px; border-left: 1px solid var(--navy);
    font-size: 10px; line-height: 15px; color: var(--ink);
  }
  .contact-row { display: flex; align-items: center; gap: 6px; }
  .contact-row svg { width: 10px; height: 10px; fill: var(--navy); flex: none; }
  .letter {
    position: absolute; left: 80px; top: 220px; width: 450px;
    font-size: 11px; line-height: 15px; color: var(--muted);
  }
  .letter-date { margin-bottom: 22px; }
  .recipient { margin-bottom: 14px; }
  .greeting { font-size: 14px; font-weight: 700; color: var(--ink); margin-bottom: 10px; }
  .letter p { margin-bottom: 16px; }
  .closing { margin-top: 24px; }
  .signature {
    font-family: "Kaushan Script", cursive;
    font-size: 34px; color: var(--ink); margin-top: 10px; margin-left: 20px;
  }
  .footer-band { position: absolute; left: 0; bottom: 0; width: 600px; height: 22px; }
</style>
</head>
<body>
  <main class="letterhead">
    <header>
      <div class="brand">
        <span class="brand-square"></span>
        <span class="brand-name">Tellwick Asset Management</span>
      </div>
      <address class="contact" style="font-style:normal">
        <div>2740 Harlow Ave, Ste</div>
        <div>100, Dallas, TX 75204</div>
        <div class="contact-row">
          <svg viewBox="0 0 10 10"><path d="M2 1l2 2-1 1.3c.6 1.2 1.5 2.1 2.7 2.7L7 6l2 2-1.3 1.5C4.5 9.2.8 5.5.5 2.3z"/></svg>555-014-2287
        </div>
        <div class="contact-row">
          <svg viewBox="0 0 10 10"><path d="M0 2h10v6H0z M0 2l5 3.5L10 2" stroke="#fff" stroke-width=".8"/></svg>info@tellwick-mail.com
        </div>
        <div class="contact-row">
          <svg viewBox="0 0 10 10"><circle cx="5" cy="5" r="4.5"/></svg>www.tellwick-web.com
        </div>
      </address>
    </header>

    <section class="letter">
      <div class="letter-date">Feb-03-2022</div>
      <div class="recipient">Mr. Alan Reeve<br>President</div>
      <div class="recipient">Marlow Corporation<br>123 Street Name, Suite# 10<br>City, State, 120023</div>
      <div class="greeting">Dear Mr. Alan</div>
      <p>Lorem ipsum dolor sit amet, consectetur adipisicing elit, sed do eiusmod tempor incididunt ut labore et dolore magna aliqua. Ut enim ad minim veniam, quis nostrud exercitation ullamco laboris nisi ut aliquip ex ea commodo consequat. Duis aute irure dolor in reprehenderit in voluptate velit esse cillum dolore eu fugiat nulla pariatur.</p>
      <p>Lorem ipsum dolor sit amet, consectetur adipisicing elit, sed do eiusmod tempor incididunt ut labore et dolore magna aliqua. Ut enim ad minim veniam, quis nostrud exercitation ullamco laboris nisi ut aliquip ex ea commodo consequat. Duis aute irure dolor in reprehenderit in voluptate velit esse cillum dolore eu fugiat nulla pariatur.</p>
      <p>Lorem ipsum dolor sit amet, consectetur adipisicing elit, sed do eiusmod tempor incididunt ut labore et dolore magna aliqua. Ut enim ad minim veniam, quis nostrud exercitation ullamco laboris nisi ut aliquip ex ea commodo consequat.</p>
      <p>Excepteur sint occaecat cupidatat non proident, sunt in culpa qui officia deserunt mollit anim id est laborum. re et dolore magnam aliquam quaerat voluptatem.</p>
      <div class="closing">Regards</div>
      <div class="signature">Daniel Hart</div>
    </section>

    <svg class="footer-band" viewBox="0 0 600 22" preserveAspectRatio="none" aria-hidden="true">
      <polygon points="448,0 600,0 600,22 436,22" fill="var(--rule-grey)"/>
      <polygon points="0,8 440,8 432,22 0,22" fill="var(--navy)"/>
    </svg>
  </main>
</body>
</html>
```